Design business card for Bright Harbour Coaching!

I am a personal development coach (like a life coach) and corporate trainer and need a professionally designed double sided business card.

It needs to contain the business logo (I'm happy for the designer to choose the layout of the logo as I am still working out the best option myself) and the following information:

Corinne Vashti
Personal Development Coach and Trainer

+61 (0)452 918 637 (written that way)
corinne@bright-harbour.example

www.bright-harbour.example

```html
<!DOCTYPE html>
<html lang="en">
<head>
<meta charset="utf-8">
<title>Bright Harbour Coaching – Business Card</title>
<link href="https://fonts.googleapis.com/css2?family=Arimo:wght@400;700&display=swap" rel="stylesheet">
<style>
  :root {
    --teal: #17959f;
    --teal-deep: #0c7f89;
    --teal-light: #2aaab3;
    --grey: #8b8e92;
    --ink: #5a5d61;
    --white: #ffffff;
    --page: #ededed;
  }
  * { box-sizing: border-box; margin: 0; padding: 0; }
  html, body {
    width: 1200px;
    height: 950px;
    overflow: hidden;
    background: var(--page);
    font-family: "Arimo", Arial, sans-serif;
  }
  .sheet {
    position: relative;
    width: 1200px;
    height: 950px;
  }
  .card {
    position: absolute;
    left: 250px;
    width: 700px;
    height: 400px;
    overflow: hidden;
    box-shadow: 0 6px 18px rgba(0,0,0,0.18);
  }
  .card--back { top: 55px; background: var(--teal); }
  .card--front { top: 495px; background: var(--teal); }

  /* back side */
  .back-brand {
    position: absolute;
    top: 145px;
    left: 0;
    width: 100%;
    display: flex;
    align-items: center;
    justify-content: center;
    gap: 14px;
  }
  .back-brand__dot {
    flex: none;
    width: 24px;
    height: 24px;
    border-radius: 50%;
    background: var(--white);
  }
  .back-brand__name {
    color: var(--white);
    font-weight: 400;
    font-size: 26px;
    letter-spacing: 1px;
    white-space: nowrap;
  }
  .back-url {
    position: absolute;
    top: 290px;
    left: 0;
    width: 100%;
    display: flex;
    align-items: center;
    justify-content: center;
    gap: 18px;
    color: var(--white);
    font-size: 15px;
    letter-spacing: 4px;
  }
  .back-url__rule {
    width: 110px;
    height: 1px;
    background: rgba(255,255,255,0.85);
  }

  /* front side */
  .front-shape { position: absolute; inset: 0; }
  .front-brand {
    position: absolute;
    top: 88px;
    left: 420px;
    width: 250px;
    display: flex;
    flex-direction: column;
    align-items: center;
    gap: 10px;
  }
  .front-brand__dot {
    flex: none;
    width: 20px;
    height: 20px;
    border-radius: 50%;
    background: var(--teal);
  }
  .front-brand__name {
    color: var(--ink);
    font-weight: 400;
    font-size: 19px;
    letter-spacing: 0.5px;
    white-space: nowrap;
  }
  .holder {
    position: absolute;
    left: 42px;
    top: 150px;
    color: var(--white);
  }
  .holder__name {
    font-weight: 700;
    font-size: 21px;
    margin-bottom: 6px;
  }
  .holder__role {
    font-size: 15px;
    line-height: 1.3;
  }
  .contact {
    position: absolute;
    left: 42px;
    bottom: 34px;
    list-style: none;
    color: var(--white);
    font-size: 15px;
    line-height: 1.45;
  }
</style>
</head>
<body>
<main class="sheet">

  <section class="card card--back" aria-label="Business card, back">
    <div class="back-brand">
      <span class="back-brand__dot"></span>
      <span class="back-brand__name">Bright Harbour Coaching</span>
    </div>
    <div class="back-url">
      <span class="back-url__rule"></span>
      <span>www.bright-harbour.example</span>
      <span class="back-url__rule"></span>
    </div>
  </section>

  <section class="card card--front" aria-label="Business card, front">
    <svg class="front-shape" viewBox="0 0 700 400" width="700" height="400" aria-hidden="true">
      <path d="M330 0 C 280 190, 430 345, 700 352 L 700 400 L 700 0 Z" fill="var(--teal-light)"/>
      <path d="M338 0 C 292 188, 440 335, 700 338 L 700 0 Z" fill="var(--grey)"/>
      <path d="M344 0 C 300 186, 446 328, 700 330 L 700 0 Z" fill="var(--white)"/>
      <path d="M354 0 C 316 170, 450 312, 700 318" fill="none" stroke="var(--teal-deep)" stroke-width="3"/>
      <path d="M360 0 C 326 162, 456 304, 700 310" fill="none" stroke="var(--white)" stroke-width="2"/>
    </svg>

    <div class="front-brand">
      <span class="front-brand__dot"></span>
      <span class="front-brand__name">Bright Harbour Coaching</span>
    </div>

    <div class="holder">
      <h1 class="holder__name">Corinne Vashti</h1>
      <p class="holder__role">Personal Development<br>Coach &amp; Trainer</p>
    </div>

    <ul class="contact">
      <li>+61 (0)452 918 637</li>
      <li>corinne@bright-harbour.example</li>
      <li>www.bright-harbour.example</li>
    </ul>
  </section>

</main>
</body>
</html>
```